Re-Design Korbalex.com make it more professional looking

We want to re-design this website, we are currently not happy with existing design. Some of the design examples are listed below.

https://trelvan.com/
https://www.quostel.com/
https://www.namity.com/projects/
https://www.flarnside.com/

The content on the website is final, there will be no change in the content. We just need to re-design the site. Features page on the site is very important and need to be layout very well.

Industry/Entity Type

It Professional

Number of Pages Required

4 page

Font styles to use
Sans Serif

Requirements
Must have
• Professional look and design like the examples i quoted above and a nice color theme. I do not have preferences but i like the quostel.com and trelvan.com

```html
<!DOCTYPE html>
<html lang="en">
<head>
<meta charset="utf-8">
<title>Korbalex – SEO Project Management</title>
<link href="https://fonts.googleapis.com/css2?family=Dosis:wght@400;500;600&display=swap" rel="stylesheet">
<style>
:root{
  --orange:#f7941d;
  --blue:#2d9fd9;
  --band-blue:#2379c0;
  --ink:#3a3a3a;
  --muted:#8a8a8a;
  --footer:#363e4b;
  --footer-text:#c9ced6;
  --bottom:#f2f2f2;
  --white:#ffffff;
}
*{margin:0;padding:0;box-sizing:border-box}
html,body{width:1200px;height:2350px;overflow:hidden}
body{font-family:"Dosis",sans-serif;color:var(--ink);background:var(--white);position:relative}
.abs{position:absolute}

/* hero */
.hero{left:0;top:0;width:1200px;height:564px;background:linear-gradient(160deg,#6b4a30 0%,#a37a52 40%,#8a6040 70%,#4a3222 100%)}
.hero-shade{left:0;top:0;width:1200px;height:564px;background:rgba(0,0,0,.22)}
.brand{left:78px;top:20px;display:flex;align-items:center;gap:8px;font-size:32px;font-weight:600;color:var(--white)}
.brand .dot{width:22px;height:22px;border-radius:50%;background:var(--orange)}
.nav-item{position:absolute;top:31px;height:32px;line-height:32px;font-size:15px;color:var(--white)}
.nav-home{left:501px;width:89px;text-align:center;background:var(--orange);border-radius:16px}
.nav-login{left:1034px;width:89px;text-align:center;border:1.5px solid var(--white);border-radius:16px;line-height:29px}
.hero-title{left:0;width:1200px;top:208px;text-align:center;font-size:33px;color:var(--white);font-weight:400}
.hero-sub{left:0;width:1200px;top:254px;text-align:center;font-size:18px;color:var(--white)}
.signup{left:357px;top:320px;width:484px;height:37px;background:var(--white);border-radius:19px;overflow:hidden;display:flex}
.signup-input{flex:1;padding-left:18px;line-height:37px;font-size:13px;color:#555}
.signup-btn{width:177px;background:var(--orange);color:var(--white);font-size:13px;font-weight:600;line-height:37px;padding-left:16px;position:relative}
.signup-btn span{position:absolute;right:10px;top:9px;width:19px;height:19px;border-radius:50%;background:#b86a0c}

/* tool intro */
.intro-art{left:160px;top:606px;width:420px;height:400px;background:radial-gradient(circle at 50% 55%,#e6e6e6 0%,#f1f1f1 45%,#f8f8f8 75%,#ffffff 100%)}
.intro-title{left:636px;top:722px;font-size:23px;color:#5a5a5a;line-height:30px;font-weight:400}
.btn-blue{left:636px;top:808px;width:169px;height:32px;line-height:32px;text-align:center;border-radius:16px;background:var(--blue);color:var(--white);font-size:14px}

/* features */
.features{left:0;top:1006px;width:1200px;height:412px;background:linear-gradient(120deg,#1f2732 0%,#3b4652 45%,#2c3540 100%)}
.features-kicker{left:0;width:1200px;top:1052px;text-align:center;font-size:13px;letter-spacing:1px;color:var(--white)}
.features-title{left:0;width:1200px;top:1082px;text-align:center;font-size:26px;color:var(--blue);font-weight:400}
.feature{display:flex;align-items:center;gap:12px;color:var(--white);font-size:14px;line-height:19px}
.feature-icon{width:52px;height:52px;border:1.5px solid var(--white);border-radius:50%;display:flex;align-items:center;justify-content:center}

/* testimonial */
.t-title{left:0;width:1200px;top:1462px;text-align:center;font-size:24px;color:var(--blue);font-weight:400}
.t-sub{left:0;width:1200px;top:1494px;text-align:center;font-size:17px;color:#999}
.avatar{left:559px;top:1551px;width:78px;height:78px;border-radius:50%;background:linear-gradient(#c98c6a,#8a5a44);border:3px solid #eee}
.quote{left:155px;top:1652px;width:890px;text-align:center;font-size:13px;line-height:17.5px;color:#777}
.t-name{left:0;width:1200px;top:1748px;text-align:center;font-size:14px;color:#333}
.t-role{left:0;width:1200px;top:1767px;text-align:center;font-size:12px;color:#999}

/* cta */
.cta{left:0;top:1868px;width:1200px;height:162px;background:var(--band-blue)}
.cta-text{left:0;width:1200px;top:1907px;text-align:center;font-size:25px;color:var(--white)}
.btn-orange{left:495px;top:1962px;width:210px;height:31px;line-height:31px;text-align:center;background:var(--orange);color:var(--white);font-size:14px}

/* footer */
.footer{left:0;top:2030px;width:1200px;height:257px;background:var(--footer)}
.f-brand{left:154px;top:2088px;display:flex;align-items:center;gap:8px;font-size:32px;font-weight:600;color:#c7ccd3}
.f-brand .dot{width:22px;height:22px;border-radius:50%;background:#8d949e}
.f-col{top:2078px;color:var(--footer-text);font-size:13.5px}
.f-col h4{font-weight:500;font-size:14px;color:var(--white);margin-bottom:10px}
.f-col li{list-style:none;line-height:21.6px}
.f-col li::before{content:"»";margin-right:7px}
.f-col li.active{color:var(--blue)}
.phone{font-size:17px;color:var(--white)}
.socials{display:flex;gap:10px;margin-top:8px}
.socials span{width:20px;height:20px;background:#d5d9df;border-radius:2px}
.socials span.active{background:var(--blue)}
.bottom{left:0;top:2287px;width:1200px;height:63px;background:var(--bottom)}
.copy{left:152px;top:2310px;font-size:13px;color:#555}
.back-top{left:884px;top:2310px;font-size:13px;color:var(--orange);text-decoration:underline}
</style>
</head>
<body>

<!-- hero -->
<div class="abs hero" role="img" aria-label="Desk workspace photo with glasses, coffee cup, plant and a hand sketching brand strategy notes"></div>
<div class="abs hero-shade"></div>
<div class="abs brand"><span class="dot"></span>Korbalex</div>
<div class="nav-item nav-home">Home</div>
<div class="nav-item" style="left:618px">Features</div>
<div class="nav-item" style="left:725px">Pricing</div>
<div class="nav-item" style="left:818px">About Us</div>
<div class="nav-item" style="left:928px">Contact Us</div>
<div class="nav-item nav-login">Login</div>
<h1 class="abs hero-title">SEO is About Organize, Collaborate and Deliver !</h1>
<p class="abs hero-sub">It is a long established fact that a reader will be distracted by the readable content of a page when looking.</p>
<div class="abs signup">
  <div class="signup-input">Enter your business email</div>
  <div class="signup-btn">Get started for free<span></span></div>
</div>
<svg class="abs" style="left:590px;top:500px" width="16" height="16" viewBox="0 0 16 16"><path d="M3 3l5 5 5-5M3 8l5 5 5-5" stroke="#fff" stroke-width="1.6" fill="none"/></svg>

<!-- tool intro -->
<svg class="abs" style="left:0;top:564px" width="1200" height="442" viewBox="0 564 1200 442">
  <path d="M104 760 L78 786 L104 812" stroke="#555" stroke-width="2" fill="none"/>
  <path d="M1096 760 L1122 786 L1096 812" stroke="#222" stroke-width="2" fill="none"/>
</svg>
<div class="abs intro-art" role="img" aria-label="Illustration of a magnifying glass over the word SEO, surrounded by role icons for client, marketer, optimizer, copy writer and designer"></div>
<h2 class="abs intro-title">Best Project Management Tool for<br>Digital Agencies</h2>
<div class="abs btn-blue">Start Your Free Trial</div>

<!-- features -->
<div class="abs features" role="img" aria-label="Dimmed photo of a team working at a laptop"></div>
<div class="abs features-kicker">FEATURES</div>
<h2 class="abs features-title">The Components You Need, Together on One Tool</h2>

<div class="abs feature" style="left:153px;top:1162px"><span class="feature-icon"><svg width="20" height="20"><circle cx="10" cy="6" r="4" fill="#fff"/><path d="M3 18q7-11 14 0z" fill="#fff"/></svg></span>Project<br>Management</div>
<div class="abs feature" style="left:381px;top:1162px"><span class="feature-icon"><svg width="22" height="20"><path d="M2 16a9 9 0 0 1 18 0z" fill="#fff"/></svg></span>Constructive<br>Dashboard</div>
<div class="abs feature" style="left:612px;top:1162px"><span class="feature-icon"><svg width="22" height="20"><rect x="2" y="3" width="18" height="13" fill="none" stroke="#fff" stroke-width="2"/><rect x="5" y="6" width="12" height="2" fill="#fff"/></svg></span>User level<br>Interface</div>
<div class="abs feature" style="left:840px;top:1162px"><span class="feature-icon"><svg width="20" height="20"><rect x="4" y="9" width="12" height="9" fill="#fff"/><path d="M6 9V6a4 4 0 0 1 8 0v3" stroke="#fff" stroke-width="2" fill="none"/></svg></span>Password<br>Manager</div>

<div class="abs feature" style="left:153px;top:1239px"><span class="feature-icon"><svg width="20" height="20"><circle cx="6" cy="6" r="4" fill="none" stroke="#fff" stroke-width="2.5"/><circle cx="14" cy="14" r="4" fill="none" stroke="#fff" stroke-width="2.5"/></svg></span>Link<br>Manager</div>
<div class="abs feature" style="left:381px;top:1239px"><span class="feature-icon"><svg width="22" height="20"><circle cx="11" cy="6" r="4" fill="#fff"/><circle cx="4" cy="9" r="3" fill="#fff"/><circle cx="18" cy="9" r="3" fill="#fff"/><path d="M3 18q8-10 16 0z" fill="#fff"/></svg></span>Client<br>Management</div>
<div class="abs feature" style="left:612px;top:1239px"><span class="feature-icon"><svg width="20" height="20"><rect x="3" y="2" width="14" height="16" fill="none" stroke="#fff" stroke-width="2"/><path d="M5 15l4-5 3 3 3-4" stroke="#fff" stroke-width="2" fill="none"/></svg></span>Customize<br>Brand</div>
<div class="abs feature" style="left:840px;top:1239px"><span class="feature-icon"><svg width="20" height="20"><rect x="3" y="6" width="10" height="12" fill="none" stroke="#fff" stroke-width="2"/><rect x="7" y="2" width="10" height="12" fill="none" stroke="#fff" stroke-width="2"/></svg></span>Billing<br>Management</div>

<div class="abs feature" style="left:153px;top:1315px"><span class="feature-icon"><svg width="20" height="20"><rect x="2" y="2" width="16" height="16" fill="none" stroke="#fff" stroke-width="1.6"/><rect x="5" y="10" width="2" height="6" fill="#fff"/><rect x="9" y="6" width="2" height="10" fill="#fff"/><rect x="13" y="8" width="2" height="8" fill="#fff"/></svg></span>Milestone<br>Management</div>
<div class="abs feature" style="left:381px;top:1315px"><span class="feature-icon"><svg width="20" height="20"><rect x="2" y="4" width="16" height="14" fill="none" stroke="#fff" stroke-width="2"/><path d="M6 11l3 3 5-6" stroke="#fff" stroke-width="2" fill="none"/></svg></span>Event<br>Management</div>
<div class="abs feature" style="left:612px;top:1315px"><span class="feature-icon"><svg width="22" height="20"><path d="M2 4h7l2 2h9v11H2z" fill="#fff"/></svg></span>File<br>Manager</div>
<div class="abs feature" style="left:840px;top:1315px"><span class="feature-icon"><svg width="20" height="20"><rect x="2" y="3" width="16" height="3" fill="#fff"/><rect x="2" y="9" width="16" height="3" fill="#fff"/><rect x="2" y="15" width="16" height="3" fill="#fff"/></svg></span>Task<br>Management</div>

<!-- testimonial -->
<h2 class="abs t-title">Still Not Sure?</h2>
<p class="abs t-sub">Here's what they have to say about us</p>
<div class="abs avatar" role="img" aria-label="Portrait photo of the reviewer"></div>
<p class="abs quote">"I have been handling SEO projects for the last 10 years. Korbalex SEO project management application is the first tool that is solely designed keeping in mind the needs of modern Search Engine Optimization. It has everything that SEO analyst needs, features like Time Management, Milestone Management, Team Management, Mail Management etc. All these make it easy to manage your workforce and deliver above the client satisfaction. Can't Ask for More – Right! Thank you Korbalex and its fantastic team! "</p>
<p class="abs t-name">Daniel Orvesto</p>
<p class="abs t-role">- Marketing Director at Stayline-suites -</p>
<svg class="abs" style="left:560px;top:1813px" width="80" height="10">
  <g fill="#ccc"><circle cx="6" cy="5" r="2.5"/><circle cx="18" cy="5" r="2.5"/><circle cx="30" cy="5" r="2.5"/><circle cx="42" cy="5" r="2.5"/><circle cx="70" cy="5" r="2.5"/></g>
  <circle cx="58" cy="5" r="3" fill="#2d9fd9"/>
</svg>

<!-- cta -->
<div class="abs cta"></div>
<p class="abs cta-text">Share your experience with us and get 3 months of premium access for free</p>
<div class="abs btn-orange">Start My 30 Day Free Trial</div>

<!-- footer -->
<div class="abs footer"></div>
<div class="abs f-brand"><span class="dot"></span>Korbalex</div>
<div class="abs f-col" style="left:381px">
  <h4>Quick Link</h4>
  <ul><li>Home</li><li class="active">About Us</li><li>Features</li><li>Pricing</li><li>Contact Us</li><li>Sitemap</li></ul>
</div>
<div class="abs f-col" style="left:611px">
  <h4>Resources</h4>
  <ul><li>Testimonials</li><li>3rd Party Apps</li><li>Newsletters</li><li>Support &amp; FAQs</li><li>Privacy Policy</li><li>Refund Policy</li></ul>
</div>
<div class="abs f-col" style="left:841px">
  <h4>Help &amp; Support</h4>
  <div class="phone">+1-555-014-2297</div>
  <div>help@korbalex.com</div>
  <h4 style="margin:12px 0 0">Follow Us</h4>
  <div class="socials"><span></span><span class="active"></span><span></span><span></span></div>
</div>
<div class="abs bottom"></div>
<p class="abs copy">© 2016, Korbalex by Brightorb Services Pvt. Ltd. All Rights Reserved.</p>
<p class="abs back-top">Back to Top ↑</p>

</body>
</html>
```